How do I determine which religion is correct?

This Infographic is part of the series "The Copper Lantern" found on my website www.brightmeadowpath.org.
This flow chart demonstrates a logical progression to determine which religion is correct based on historical factors and communication from the greatest conceivable being or God.

The main part of the sheet is the thought process starting with the question "How to I determine which religion is correct?"
The first question "Is the religion extant?" That is does the religion still exist. To the left you see no, these are defunct religions. To the right yes are religions that still exist and so pass on through the next question.

There are 5 main questions. The religions that get a no go into the "discarded bin" and the yes pass into the next question. Kind of like a funnel. Until the the end
The last question "Is there one eternal creator being?" Should be "Does the religion teach one eternal greatest conceivable being?" Also Hinduism should go to the "Yes" side not the no.

The 5 questions with the triangle have corresponding articles on the website. Also the right most questions in the flag-like box also have articles on the website and are associated with the question to the left. These articles and question provide more information.

This infographic is a quick reference to understand the thought process. I kind of like the idea of a funnel and waste basket, but I don't want to limit your creativity. I really like what you did on my last project, your design was beyond my best hopes.

If somehow these questions could be clickable links to the website that would be amazing.

```html
<!DOCTYPE html>
<html lang="en">
<head>
<meta charset="utf-8">
<title>The Copper Lantern – How do I determine which religion is correct?</title>
<link href="https://fonts.googleapis.com/css2?family=Bebas+Neue&family=Roboto:wght@500;700;900&display=swap" rel="stylesheet">
<style>
  :root{
    --orange:#fbb040;
    --purple:#7e5a8c;
    --teal:#006582;
    --ink:#333338;
    --chip:#eeeef2;
    --side:#efeff3;
    --rule:#8a8a90;
    --emblem-a:#3a8fd6;
    --emblem-b:#1458b8;
  }
  *{box-sizing:border-box;margin:0;padding:0}
  html,body{width:1200px;height:927px;overflow:hidden}
  body{font-family:"Roboto",Arial,sans-serif;position:relative;
    background:linear-gradient(135deg,#fde3c2 0%,#f6efea 25%,#e8e6f0 45%,#f6f6fa 75%,#f9f9fc 100%);}
  a{color:inherit;text-decoration:none}

  .masthead{position:absolute;left:0;top:0;width:1003px;height:59px;background:var(--orange)}
  .masthead h1{position:absolute;left:62px;top:6px;font-family:"Bebas Neue",Impact,sans-serif;font-weight:400;
    font-size:46px;line-height:1;color:#fff;letter-spacing:1px;text-shadow:2px 2px 0 var(--purple)}
  .question-band{position:absolute;left:0;top:59px;width:1003px;height:42px;background:var(--purple)}
  .question-band h2{position:absolute;left:60px;top:7px;font-size:27px;font-weight:900;color:#fff;letter-spacing:.6px}

  .sidebar{position:absolute;left:1003px;top:0;width:197px;height:927px;background:var(--side)}
  .sidebar-head{height:59px;background:var(--purple);color:#fff;font-weight:700;font-size:16.5px;padding:20px 0 0 13px}
  .article{position:absolute;left:0;width:197px;border-bottom:1px solid var(--rule);padding-left:25px;
    display:flex;flex-direction:column;justify-content:center;gap:10px;font-size:15.5px;font-weight:700;color:var(--ink);line-height:1.18}

  .spine{position:absolute;left:381px;top:101px;width:2px;height:650px;background:var(--ink)}
  .spine-dot{position:absolute;left:376px;top:96px;width:11px;height:11px;border-radius:50%;background:#fff;border:2px solid var(--purple)}
  .arrow{position:absolute;left:375px;width:0;height:0;border-left:7px solid transparent;border-right:7px solid transparent;border-top:14px solid var(--purple)}

  .step{position:absolute;left:0;width:1003px;height:78px}
  .discard{position:absolute;left:26px;top:0;width:230px;height:78px;border-radius:39px;background:var(--purple);
    color:#fff;font-size:16.5px;font-weight:500;line-height:1.2;display:flex;align-items:center;justify-content:center;text-align:center;padding-right:40px}
  .pass{position:absolute;left:505px;top:0;width:467px;height:78px;border-radius:39px;background:var(--teal);
    color:#fff;font-size:16.5px;font-weight:500;line-height:1.22;display:flex;align-items:center;justify-content:center;text-align:center;padding-left:30px}
  .query{position:absolute;left:240px;top:14px;width:280px;height:50px;background:#fff;box-shadow:0 1px 4px rgba(0,0,0,.08);
    display:flex;align-items:center;justify-content:center;text-align:center;font-size:19.5px;font-weight:700;color:var(--ink);line-height:1.05;padding:0 26px}
  .query.long{top:5px;height:68px;font-size:16px;line-height:1.12}
  .chip{position:absolute;top:14px;width:50px;height:50px;border-radius:50%;background:var(--chip);border:2px solid #fff;
    box-shadow:0 1px 3px rgba(0,0,0,.15);display:flex;align-items:center;justify-content:center;font-size:16px;font-weight:700;z-index:2}
  .chip.no{left:217px;color:var(--purple)}
  .chip.yes{left:494px;color:var(--teal)}

  .verdict{justify-content:flex-end;padding-right:40px;font-size:23px;font-weight:900;line-height:1.1}
  .emblem{position:absolute;left:597px;top:-87px;width:160px;height:166px;background:#fff;border-radius:80px 80px 0 0;
    display:flex;align-items:flex-end;justify-content:center;padding-bottom:20px}
  .emblem-fill{width:100px;height:110px;border-radius:50px 50px 8px 8px;
    background:linear-gradient(160deg,var(--emblem-a),var(--emblem-b));opacity:.85}
</style>
</head>
<body>
  <header class="masthead"><h1>THE COPPER LANTERN</h1></header>
  <div class="question-band"><h2>HOW DO I DETERMINE WHICH RELIGION IS CORRECT?</h2></div>

  <div class="spine"></div>
  <div class="spine-dot"></div>
  <div class="arrow" style="top:131px"></div>
  <div class="arrow" style="top:266px"></div>
  <div class="arrow" style="top:406px"></div>
  <div class="arrow" style="top:546px"></div>
  <div class="arrow" style="top:690px"></div>

  <section class="step" style="top:163px">
    <div class="discard">Greek &amp;<br>Roman etc</div>
    <div class="pass">Christianity, Islam, Hinduism, Buddhism, Judaism,<br>Chinese Tradition, African Tradition, Ethnic Religions,<br>Sikhism, Jainism, Zoroastrianism</div>
    <a class="query" href="https://www.brightmeadowpath.org">Is the religion extant?</a>
    <div class="chip no">NO</div><div class="chip yes">YES</div>
  </section>

  <section class="step" style="top:301px">
    <div class="discard">Islam, Christianity<br>&amp; Sikhism</div>
    <div class="pass">Hinduism, Buddhism, Judaism, Jainism, Chinese<br>Tradition, African Tradition, Ethnic Religions,<br>Zoroastrianism</div>
    <a class="query" href="https://www.brightmeadowpath.org">Is the religion old?</a>
    <div class="chip no">NO</div><div class="chip yes">YES</div>
  </section>

  <section class="step" style="top:443px">
    <div class="discard">Chinese/African<br>Tradition, Ethnic</div>
    <div class="pass">Hinduism, Buddhism, Judaism,<br>Jainism, Zoroastrianism</div>
    <a class="query" href="https://www.brightmeadowpath.org">Is there a written<br>Tradition?</a>
    <div class="chip no">NO</div><div class="chip yes">YES</div>
  </section>

  <section class="step" style="top:591px">
    <div class="discard">Buddhism,<br>Zoroastrianism</div>
    <div class="pass">Judaism, Hinduism, Jainism</div>
    <a class="query" href="https://www.brightmeadowpath.org">Does religion claim &gt;1<br>communication?</a>
    <div class="chip no">NO</div><div class="chip yes">YES</div>
  </section>

  <section class="step" style="top:741px">
    <div class="discard">Jainism</div>
    <div class="pass verdict">JUDAISM &amp;<br>HINDUISM</div>
    <div class="emblem">
      <div class="emblem-fill" role="img" aria-label="Emblem for the religions that pass every question"></div>
    </div>
    <a class="query long" href="https://www.brightmeadowpath.org">Does the religion teach one eternal greatest conceivable being?</a>
    <div class="chip no">NO</div><div class="chip yes">YES</div>
  </section>

  <aside class="sidebar">
    <div class="sidebar-head">Articles on the website</div>
    <a class="article" href="https://www.brightmeadowpath.org" style="top:59px;height:88px;gap:8px">
      <span>What is God Series?</span><span>What is the purpose of communication?</span></a>
    <a class="article" href="https://www.brightmeadowpath.org" style="top:147px;height:121px">
      <span>Why must the<br>religion still exist?</span></a>
    <a class="article" href="https://www.brightmeadowpath.org" style="top:268px;height:141px">
      <span>Why must the<br>religion be old?</span></a>
    <a class="article" href="https://www.brightmeadowpath.org" style="top:409px;height:142px">
      <span>Why is a written<br>tradition important?</span></a>
    <a class="article" href="https://www.brightmeadowpath.org" style="top:551px;height:135px">
      <span>Why does 2 or more<br>communications<br>matter?</span></a>
    <a class="article" href="https://www.brightmeadowpath.org" style="top:686px;height:180px;border-bottom:none;gap:16px">
      <span>Why must there be a<br>first cause?</span><span>Why does God have to<br>be the creator?</span><span>Does something<br>have to be eternal?</span></a>
  </aside>
</body>
</html>
```